Web Button design and production

I need remote control like buttons (or your own design of buttons if I like it)
3x4 text buttons (normal, pressed, disabled)
3x1 empty button (normal, pressed, disabled)
3x6 buttons with glyph (normal, pressed, disabled)
3x288 with 24h time "00:00", "00:05", "00:10" (normal, pressed, disabled)
4 LED (red, green, orange, black)
I will upload the background image as soon as possible (black plastic)
See attached images
Q: Do the buttons have to be gray/black?
A: It should look like a high end remote control. It could be brushed aluminum as well, or something you come up with. But I guess black or dark grey would be best. The background will be pixelvaultimages 40631758, but it's not available yet.
Q: Do I have to provide all buttons for the contest?
A: No! I only need one button (3 states) and a LED to decide. Only the winner will do the whole job.
Q: Is the Designer who wins the contest expected to complete all the extra buttons?
A: Yes, please.
Plastic

```html
<!DOCTYPE html>
<html lang="en">
<head>
<meta charset="utf-8">
<title>Remote Control Buttons</title>
<link rel="stylesheet" href="https://fonts.googleapis.com/css2?family=PT+Sans:wght@400&display=swap">
<style>
  :root {
    --bg-center: #ffffff;
    --bg-edge: #e4e4e4;
    --face-top: #4c4c4c;
    --face-bottom: #2b2b2b;
    --face-edge: #1c1c1c;
    --side: #161616;
    --label: #ffffff;
    --label-disabled: #5e5e5e;
    --led-green: #7cc242;
    --led-amber: #f7c11a;
    --led-red: #e0212b;
    --led-black: #111111;
  }
  * { box-sizing: border-box; margin: 0; padding: 0; }
  html, body { width: 1200px; height: 900px; overflow: hidden; }
  body {
    position: relative;
    background: radial-gradient(ellipse 70% 70% at 50% 45%, var(--bg-center) 0%, #f6f6f6 55%, var(--bg-edge) 100%);
    font-family: "PT Sans", sans-serif;
  }
  .button {
    position: absolute;
    width: 246px;
    height: 144px;
    border-radius: 18px;
    background: linear-gradient(180deg, var(--face-top) 0%, #3a3a3a 45%, var(--face-bottom) 100%);
    border: 2px solid var(--face-edge);
    box-shadow: 0 9px 0 var(--side), 0 11px 6px rgba(0,0,0,0.25);
    overflow: hidden;
    display: flex;
    align-items: center;
    justify-content: center;
    color: var(--label);
  }
  .button::before {
    content: "";
    position: absolute;
    left: -30%;
    top: -62%;
    width: 160%;
    height: 110%;
    border-radius: 50%;
    background: linear-gradient(180deg, rgba(255,255,255,0.16) 0%, rgba(255,255,255,0.05) 100%);
  }
  .button::after {
    content: "";
    position: absolute;
    left: 10px; right: 10px; top: 4px;
    height: 2px;
    border-radius: 2px;
    background: rgba(255,255,255,0.18);
  }
  .button--pressed {
    width: 240px;
    height: 142px;
    box-shadow: 0 5px 0 var(--side), 0 6px 4px rgba(0,0,0,0.25);
  }
  .button--disabled { color: var(--label-disabled); }
  .label { position: relative; z-index: 1; line-height: 1; }
  .label--word { font-size: 80px; margin-top: 4px; }
  .label--time { font-size: 70px; margin-top: 4px; letter-spacing: -1px; }
  .glyph { position: relative; z-index: 1; width: 76px; height: 78px; }
  .glyph polygon { fill: currentColor; }

  .col-1 { left: 114px; }
  .col-2 { left: 400px; }
  .col-3 { left: 676px; }
  .row-1 { top: 170px; }
  .row-2 { top: 374px; }
  .row-3 { top: 580px; }
  .col-2.row-1 { top: 178px; }
  .col-2.row-2 { top: 382px; }
  .col-2.row-3 { top: 588px; }

  .led {
    position: absolute;
    width: 26px; height: 26px;
    border-radius: 50%;
    box-shadow: 0 2px 3px rgba(0,0,0,0.3);
  }
  .led--green { left: 987px; top: 191px; background: radial-gradient(circle at 38% 32%, #d6f0b8 0%, var(--led-green) 45%, #4c8a1e 100%); }
  .led--amber { left: 1099px; top: 191px; background: radial-gradient(circle at 38% 32%, #fff2b0 0%, var(--led-amber) 45%, #c48a00 100%); }
  .led--red { left: 987px; top: 283px; background: radial-gradient(circle at 38% 32%, #ffb3b3 0%, var(--led-red) 45%, #9a0c12 100%); }
  .led--black { left: 1099px; top: 283px; background: radial-gradient(circle at 38% 32%, #777 0%, var(--led-black) 45%, #000 100%); }
</style>
</head>
<body>
  <div class="button col-1 row-1" aria-label="Play, normal">
    <svg class="glyph" viewBox="0 0 76 78"><polygon points="2,2 74,39 2,76"/></svg>
  </div>
  <div class="button button--pressed col-2 row-1" aria-label="Play, pressed">
    <svg class="glyph" viewBox="0 0 76 78"><polygon points="2,2 74,39 2,76"/></svg>
  </div>
  <div class="button button--disabled col-3 row-1" aria-label="Play, disabled">
    <svg class="glyph" viewBox="0 0 76 78"><polygon points="2,2 74,39 2,76"/></svg>
  </div>

  <div class="button col-1 row-2"><span class="label label--word">Text</span></div>
  <div class="button button--pressed col-2 row-2"><span class="label label--word">Text</span></div>
  <div class="button button--disabled col-3 row-2"><span class="label label--word">Text</span></div>

  <div class="button col-1 row-3"><span class="label label--time">00:05</span></div>
  <div class="button button--pressed col-2 row-3"><span class="label label--time">00:05</span></div>
  <div class="button button--disabled col-3 row-3"><span class="label label--time">00:05</span></div>

  <span class="led led--green" aria-label="Green LED"></span>
  <span class="led led--amber" aria-label="Amber LED"></span>
  <span class="led led--red" aria-label="Red LED"></span>
  <span class="led led--black" aria-label="Black LED"></span>
</body>
</html>
```